Leading the way in online fitness and education requires power house web design

If you need to contact me you can do so via
skype: Travlin

We need a website designed for new company based in Houston Texas called "TravlinFit". We offer web based training and nutrition programs for our members for example we use the same software as these companies: http://marobelka.com/ http://www.liftquorra.com/ i would like my visitors to be captivated by the level of design creativity of the site.

colors to use would be grey, orange and green.
for example i like the green of this site http://www.cartbeam.com/
i will upload my logo files so you can get a feel for shades of grey and orange.

there is a 3d effect filter i would like applied to my logo for use in the web design i have uploaded what that effect looks like.

i will need your designs to be complete with all interior pages which will include Home, Fitness, Nutrition, Fit Lounge, Fit Score, Fit School, Contact Us, Sign up.

fit lounge on my site is the same as pathwick on liftquorra and locker room on marobelka just re branded.

fit school is a research corner for members to learn about health and fitness, we are members of major medical journals on health and fitness and will have all our articles be from the newest research findings.

competitor sites
these sites use same software:
http://marobelka.com/
http://www.liftquorra.com/

these sites are other software.
http://home.sprintmesa.com/software-for-athletes.aspx
http://www.vigordex.com/

here are some websites that i like:
http://www.crestwaveplay.com/
http://www.nub-lantern.com/
http://fimzol.com/
http://www.parqudo.com/
http://www.lortavi.de/fandiloop/
http://brisketmade.com/

i also like the greens in this site that i am uploading

I have been reviewing the designs and would like to update everyone at once I do not want a normal fitness website design style, no testimonials, blog post, bodyfat calculator

my website will be a membership based website. i want the website to sell the main points of my fitness app that my members will have access to look at the comments for my selling points, use those points in the site create designs and graphics to visualize those points.

look at these sites and gain inspiration

http://www.tuvelo.com.pl/#/projekty/case-studies
http://www.quendar.com/en#/home#ld-kpvm-402617-0045
http://www.nub-lantern.com/
http://fimzol.com/
http://www.parqudo.com/

i have a few designers asking me what the selling points are, the website needs to be built around these points

main selling points.

overview

programs utilize the best multi-joint exercises combined with high intensity cardio, to give you a full-body workout, efficiently and effectively. This means you’re burning more calories and building more lean muscle per unit of time than traditional weight training and cardio programs.

When you sign up, you''ll receive a work out and diet plan to fit your goals and fitness level. As you progress through your plan, you can use the personal fitness and meal calendar to record your results. When you sign-up we''ll ask you a series of questions and your workouts will be tailored to your exact needs. That means never having to use a generic diet and exercise plan again.

If you''ve ever tried to lose weight and build muscle and didn''t succeed, we feel your pain. Until now, trying to navigate all the fitness fads and latest trends on your own has been difficult. The best option - hiring a certified personal trainer - may be out of your financial reach. That''s where we come in - we''re personal trainers on a mission to help you reach your fitness goals quickly and for less money than in person training. Best of all, we''re here to help you day or night.

Fitness

Personal Fitness Calendar

Tailored to the member’s schedule and flexible to accommodate any changes to a member’s regular fitness schedule. Track your progress and stay on track with your fitness goals.

Custom Fitness Plan

Based on a member’s current physical condition and goals.

• Step by step exercise instructions
• 3-D video demonstrations of over 600 exercises, including functional and body-weight only movements
• Equipment filter can customize plans to your gym’s equipment package
• Record workouts to track exercise history and progression

Nutrition

Nutritional Assessment

Daily recommended caloric intake (Protein, Carbohydrates and Fats), based on personal profile and daily fitness plan.

Custom Meal Plan

Personalized meal plan based on nutritional assessment.

• Choose number of meals per day
• Add dietary restrictions, food preferences or dislikes
• Database of thousands of ingredients allows for hundreds of thousands of meal combinations
• Include favorite foods by entering custom nutritional information

Weight tracking

Calculate goal weight and track weight-loss or weight-gain progress. You will reach your goals in no time.

Fit Lounge

What is the most important part of any workout or fitness program? Staying motivated. And what better form of motivation than positive encouragement from your peers?

Fit Lounge is fitness focused social network for health-minded individuals looking for a simple and convenient place to track their workout goals and monitor their progress. A unique system of motivation, support and accountability makes setting fitness goals and then keeping up with them easy

Track

Start by setting fitness goals that you want to track. They can be anything from running and jogging to how many hours of sleep you are getting and how many glasses of water you are drinking every day. Other members of the travlinfits community might be tracking the same workout goals as you, so you can always join their groups as well.

Share

Once you start tracking your workout goals, you can share your progress with your friends. Reach a new max on your bench press? Let everyone know. Eclipse the 10 mile mark on your daily run? Spread the word! The communication of encouragement back and forth is a great way to ensure that everyone stays on track with their workout goals.

Achieve

Of course, the point of any workout or fitness program is to achieve the goals you’ve set. And with help from travlinfits workout tracking tools and encouragement from the community, you will achieve your workout goals in no time. When you see a friend has achieved his or her fitness goals, you can send them a virtual “fist bump” as a sign of congratulations. The number of “fist bumps” each user accumulates will be displayed on their profile, providing additional motivation and a healthy dose of competition.

Reason: i dont feel the designs i have received are of the quality i am looking for

check this website out, i know its flash, but i also know you can get creative without flash and have nice effects throughout the site.

http://www.driftlane-hub.com/

I dont want plain jane designs, insert the content i provided into the site and have it explored in a unique way. take as much time on the design as you need as i will keep extending deadline until i find one that is perfect.

as said before don't make the site anything like the competition sites, its only purpose is to sell the memberships using content provided so i need an innovative way to for them to explore that content,

as your designing this site add me on skype so i can detail and help brainstorm ideas my skype id is travlin
you can stray from the color scheme a little or throw it away if you want i just want to see how creative you can get.

Industry/Entity Type

School

Requirements
Nice to have
• if you notice at the bottom of http://marobelka.com/ she has the orange bar with the three short content parts, i like the idea of having a space like that for similar content.

on http://www.vigordex.com/ if you look to the left side of the scrolling icons i like the idea of having icons or animated pictures to point of key benefits.

```html
<!DOCTYPE html>
<html lang="en">
<head>
<meta charset="utf-8">
<title>TravlinFit – Personal Training</title>
<link href="https://fonts.googleapis.com/css2?family=Open+Sans:ital,wght@0,400;0,600;0,700;0,800;1,400;1,600&display=swap" rel="stylesheet">
<style>
:root{
  --orange:#e8540f;
  --orange-bright:#f7821c;
  --green:#1f8a1a;
  --green-dark:#0d5a0b;
  --brown:#4a3524;
  --ink:#333;
  --text:#666;
  --accent-text:#2a6a12;
  --page:#eeeeee;
}
*{box-sizing:border-box;margin:0;padding:0}
html,body{width:960px;height:1200px;overflow:hidden}
body{position:relative;background:var(--page);font-family:"Open Sans",Arial,sans-serif;color:var(--text);font-size:10.5px}
a{color:inherit;text-decoration:none}

/* header */
.site-header{position:absolute;left:0;top:0;width:960px;height:75px;background:linear-gradient(#fafafa,#e9e9e9)}
.brand{position:absolute;left:106px;top:12px;font-size:42px;font-weight:800;color:#3a3a3a;letter-spacing:-1px;line-height:1}
.util-links{position:absolute;right:104px;top:9px;font-size:10px;color:#333}
.phone{position:absolute;right:104px;top:32px;font-size:17px;color:#333}

/* nav */
.main-nav{position:absolute;left:0;top:75px;width:960px;height:38px;background:linear-gradient(#2fa326,var(--green) 50%,var(--green-dark));border-top:1px solid #8fd27e}
.main-nav ul{list-style:none}
.main-nav li{position:absolute;top:0;height:37px;line-height:37px;color:#fff;font-size:12px;font-weight:600;white-space:nowrap}
.main-nav .divider{position:absolute;top:8px;width:1px;height:22px;background:rgba(0,0,0,.25);box-shadow:1px 0 0 rgba(255,255,255,.15)}
.main-nav li.active::before{content:"";position:absolute;left:50%;top:0;margin-left:-5px;border:5px solid transparent;border-top:7px solid #fff}
.main-nav li.active::after{content:"";position:absolute;left:50%;bottom:0;margin-left:-5px;border:5px solid transparent;border-bottom:7px solid var(--orange-bright)}
.signup-btn{position:absolute;left:778px;top:7px;width:86px;height:25px;border-radius:7px;background:linear-gradient(#fff,#e6e6e6);color:#222;font-size:14px;font-weight:600;text-align:center;line-height:25px}

/* hero */
.hero-band{position:absolute;left:0;top:113px;width:960px;height:264px;background:linear-gradient(90deg,#f06c0b,#fb9a2a 50%,#f06c0b)}
.hero{position:absolute;left:96px;top:6px;width:768px;height:253px;background:#f4f4f4;overflow:hidden}
.hero-photo{position:absolute;left:0;top:0;width:768px;height:253px;background:radial-gradient(ellipse at 35% 60%,#c9a89a 0,#b08c86 20%,#d8d0cf 45%,#f3f3f3 70%)}
.hero-line{position:absolute;font-size:29px;font-weight:700;color:#555;text-shadow:1px 1px 2px rgba(0,0,0,.3);line-height:36px;white-space:nowrap}
.hero-with{position:absolute;right:59px;top:136px;font-size:14px;font-weight:700;color:#333;white-space:nowrap}
.hero-with span{color:var(--orange)}

/* thumb strip */
.thumb-strip{position:absolute;left:0;top:377px;width:960px;height:83px;background:var(--brown)}
.thumb{position:absolute;top:13px;width:141px;height:56px;border:3px solid #fff;background:linear-gradient(#8a8a8a,#4d4d4d)}
.thumb.dim{opacity:.75}
.thumb.current{background:linear-gradient(#f0f0f0,#c9b6ae)}
.thumb.current::before{content:"";position:absolute;left:62px;top:-12px;border:6px solid transparent;border-bottom:7px solid #fff}
.strip-arrow{position:absolute;top:28px;width:10px;height:24px}

/* panels */
.panel{position:absolute;left:104px;width:752px;background:#fff;box-shadow:0 0 4px rgba(0,0,0,.2)}
.panel-top{top:460px;height:227px}
.panel-bottom{top:830px;height:213px;border-radius:8px 8px 0 0}
.col{position:absolute;width:232px}
.col h2{font-size:19px;font-weight:400;color:var(--orange);line-height:24px;white-space:nowrap}
.col p.body{text-align:justify;line-height:14.3px;margin-top:4px}
.read-more{position:absolute;right:0;font-size:11px;font-weight:600;font-style:italic;color:#222;text-decoration:underline}
.feature-img{margin-top:6px;width:232px;height:78px;border:1px solid #ccc}
.apple{background:radial-gradient(circle at 50% 50%,#8ccc3a 0,#6aa82a 22%,#f2c04a 34%,#fff 55%)}
.award{background:linear-gradient(#f4f0ff,#e3dcf5)}

/* green band */
.green-band{position:absolute;left:96px;top:679px;width:768px;height:173px;border-radius:6px;background:linear-gradient(#0a5d0a,#1a8a14 55%,#0d5e0a)}
.promo{position:absolute;top:17px;width:240px;color:#fff}
.promo h3{font-size:15px;font-weight:600;line-height:18px}
.promo .pic{position:absolute;left:0;top:28px;width:103px;height:81px;border:2px solid #fff}
.promo p{position:absolute;left:117px;top:25px;width:120px;line-height:14.3px}
.lounge{background:linear-gradient(#c9a27c,#6b4a30)}
.school{background:linear-gradient(#8d8faa,#3a3b4a)}
.phone-app{background:linear-gradient(#5c8bb8,#1e2a38)}

/* fitness plan list */
.plan-item{height:52px;border-bottom:1px solid #ddd;position:relative}
.plan-item p{padding-top:7px;white-space:nowrap}
.plan-item .tag{position:absolute;left:0;top:26px;font-style:italic;color:var(--accent-text)}
.plan-item .more{position:absolute;right:2px;top:26px;font-style:italic;color:var(--accent-text)}

/* meal planning */
.meal h4{font-size:11.5px;font-weight:600;color:#333;margin-top:8px;white-space:nowrap}
.meal .sub{color:var(--accent-text);margin-top:2px}
.meal p{line-height:14.3px;margin-top:3px;text-align:justify;padding-bottom:6px;border-bottom:1px solid #ddd}
.meal p.last{border:none}

/* lounge steps */
.step{position:relative;height:84px;border-bottom:1px solid #ddd;margin-top:4px}
.step.last{border:none}
.step-icon{position:absolute;left:0;top:4px;width:56px;height:54px;border:2px solid #ddd;background:#f1f1f1}
.step-icon svg{position:absolute;left:13px;top:12px;width:26px;height:26px}
.step p{position:absolute;left:63px;top:2px;width:169px;text-align:justify;line-height:14.3px}
.step p b{color:#333;font-weight:600}
.step .more{position:absolute;right:0;top:50px;font-style:italic;color:var(--accent-text)}

/* footer */
.site-footer{position:absolute;left:0;top:1043px;width:960px;height:157px;background:linear-gradient(#333,#262626)}
.footer-label{position:absolute;top:11px;font-size:14px;color:#e8e8e8}
.email-field{position:absolute;left:113px;top:38px;width:167px;height:20px;border-radius:10px;background:linear-gradient(#555,#7a7a7a);border:1px solid #888;color:#bbb;font-style:italic;font-size:11px;line-height:18px;padding-left:8px}
.subscribe{position:absolute;left:296px;top:36px;width:113px;height:25px;border-radius:3px;background:linear-gradient(#ffb04a,#e8620c);color:#111;font-size:12px;font-weight:700;text-align:center;line-height:25px}
.social{position:absolute;top:36px;width:38px;height:38px;border:2px solid #666;border-radius:3px;background:linear-gradient(#4a4a4a,#111)}
.social span{position:absolute;left:9px;top:9px;width:16px;height:16px;border-radius:2px;background:#888}
.footer-bottom{position:absolute;left:0;top:92px;width:960px;height:65px;border-top:1px solid #1a1a1a;box-shadow:inset 0 1px 0 #444;text-align:center;color:#f0f0f0;font-size:10px;line-height:14.5px;padding-top:10px}
.footer-bottom .sep{margin:0 5px}
</style>
</head>
<body>

<header class="site-header">
  <div class="brand">TravlinFit</div>
  <div class="util-links"><a href="#">Login</a> /<a href="#">Site Map</a></div>
  <div class="phone">Call us today : &nbsp;148 506 3917</div>
</header>

<nav class="main-nav">
  <ul>
    <li class="active" style="left:113px">HOME</li>
    <li style="left:176px">FITNESS</li>
    <li style="left:252px">NUTRITION</li>
    <li style="left:345px">FIT LOUNGE</li>
    <li style="left:443px">FIT SCORE</li>
    <li style="left:530px">FIT SCHOOL</li>
    <li style="left:622px">CONTACT US</li>
  </ul>
  <span class="divider" style="left:161px"></span>
  <span class="divider" style="left:237px"></span>
  <span class="divider" style="left:330px"></span>
  <span class="divider" style="left:427px"></span>
  <span class="divider" style="left:514px"></span>
  <span class="divider" style="left:607px"></span>
  <span class="divider" style="left:704px"></span>
  <a class="signup-btn" href="#">SIGN UP</a>
</nav>

<section class="hero-band">
  <div class="hero">
    <div class="hero-photo" role="img" aria-label="Personal trainer spotting a woman lifting dumbbells on an exercise ball"></div>
    <p class="hero-line" style="left:386px;top:22px">• Get Leaner</p>
    <p class="hero-line" style="left:445px;top:61px">• Get Fitter</p>
    <p class="hero-line" style="left:505px;top:100px">• Get Stronger</p>
    <p class="hero-with">with Travlin <span>Fit</span></p>
  </div>
</section>

<section class="thumb-strip">
  <svg class="strip-arrow" style="left:104px" viewBox="0 0 10 24"><path d="M8 1 L2 12 L8 23" fill="none" stroke="#aaa" stroke-width="1.5"/></svg>
  <div class="thumb current" style="left:118px" role="img" aria-label="Trainer and client workout"></div>
  <div class="thumb" style="left:264px" role="img" aria-label="Gym training session"></div>
  <div class="thumb dim" style="left:410px" role="img" aria-label="Healthy food and measuring tape"></div>
  <div class="thumb" style="left:555px" role="img" aria-label="Weight room exercise"></div>
  <div class="thumb" style="left:700px" role="img" aria-label="Woman stretching on a mat"></div>
  <svg class="strip-arrow" style="left:846px" viewBox="0 0 10 24"><path d="M2 1 L8 12 L2 23" fill="none" stroke="#aaa" stroke-width="1.5"/></svg>
</section>

<section class="panel panel-top">
  <div class="col" style="left:9px;top:26px;height:190px">
    <h2>Welcome to Our Site</h2>
    <p class="body">Our programs combine the best multi-joint exercises with high intensity cardio for a full-body workout, done efficiently and effectively. You burn more calories and build more lean muscle per unit of time. Sign up, answer a few questions, and get a workout and diet plan tailored to your goals, plus trainers here to help you day or night.</p>
    <a class="read-more" style="top:170px" href="#">Read More</a>
  </div>
  <div class="col" style="left:260px;top:26px;height:190px">
    <h2>Nuritions</h2>
    <div class="feature-img apple" role="img" aria-label="Green apple wrapped in a measuring tape"></div>
    <p class="body">Daily recommended caloric intake of protein, carbohydrates and fats, based on your profile and fitness plan.</p>
    <a class="read-more" style="top:170px" href="#">Read More</a>
  </div>
  <div class="col" style="left:513px;top:26px;height:190px">
    <h2>Fitness Score</h2>
    <div class="feature-img award" role="img" aria-label="Physical education award certificate"></div>
    <p class="body">Calculate your goal weight and track weight-loss or weight-gain progress. You will reach your goals in no time.</p>
    <a class="read-more" style="top:170px" href="#">Read More</a>
  </div>
</section>

<section class="green-band">
  <div class="promo" style="left:17px">
    <h3>Fit Lounge</h3>
    <div class="pic lounge" role="img" aria-label="Modern lounge room"></div>
    <p>A fitness focused social network to track goals, share progress and stay motivated.</p>
  </div>
  <div class="promo" style="left:264px">
    <h3>Fit School</h3>
    <div class="pic school" role="img" aria-label="Group fitness class in a studio"></div>
    <p>A research corner built on the newest findings from major medical journals.</p>
  </div>
  <div class="promo" style="left:520px">
    <h3>Fitness on Phone</h3>
    <div class="pic phone-app" role="img" aria-label="Fitness app on smartphones"></div>
    <p>Your workouts, meal plan and fitness calendar with you day or night.</p>
  </div>
</section>

<section class="panel panel-bottom">
  <div class="col" style="left:9px;top:14px">
    <h2>Custom Fitness Plan</h2>
    <div class="plan-item"><p>Step by step exercise instructions.</p><span class="tag">Fitness Plan</span><a class="more" href="#">Learn More</a></div>
    <div class="plan-item"><p>3-D video demos of over 600 exercises.</p><span class="tag">Video Library</span><a class="more" href="#">Learn More</a></div>
    <div class="plan-item"><p>Record workouts to track progression.</p><span class="tag">Fitness Calendar</span><a class="more" href="#">Learn More</a></div>
  </div>
  <div class="col meal" style="left:256px;top:14px">
    <h2>Custom Meal Plan</h2>
    <h4>Nutritional Assessment</h4>
    <div class="sub">Protein, Carbohydrates and Fats</div>
    <p>Daily caloric intake based on your personal profile and daily fitness plan.</p>
    <h4>Meals Made for You</h4>
    <div class="sub">Thousands of ingredients</div>
    <p class="last">Choose meals per day and add dietary restrictions, preferences or dislikes.</p>
  </div>
  <div class="col" style="left:512px;top:14px">
    <h2>Track, Share, Achieve</h2>
    <div class="step">
      <div class="step-icon"><svg viewBox="0 0 26 26"><path d="M3 13 L10 20 L23 5" fill="none" stroke="#1f8a1a" stroke-width="3.5" stroke-linecap="round" stroke-linejoin="round"/></svg></div>
      <p><b>Track</b> any goal, from daily runs to hours of sleep, and join groups tracking the same goals.</p>
      <a class="more" href="#">Learn More</a>
    </div>
    <div class="step last">
      <div class="step-icon"><svg viewBox="0 0 26 26"><path d="M13 23 V4 M5 11 L13 3 L21 11" fill="none" stroke="#e8540f" stroke-width="3.5" stroke-linecap="round" stroke-linejoin="round"/></svg></div>
      <p><b>Share</b> a new max with friends and send a fist bump when they achieve their goals.</p>
      <a class="more" href="#">Learn More</a>
    </div>
  </div>
</section>

<footer class="site-footer">
  <div class="footer-label" style="left:113px">New Letter Sign Up</div>
  <div class="email-field">Enter Email Address</div>
  <a class="subscribe" href="#">Subscribe Now !</a>
  <div class="footer-label" style="left:680px">Update fitness with us</div>
  <a class="social" style="left:680px" href="#" aria-label="Social network"><span></span></a>
  <a class="social" style="left:726px" href="#" aria-label="Social network"><span></span></a>
  <a class="social" style="left:772px" href="#" aria-label="Video channel"><span></span></a>
  <a class="social" style="left:818px" href="#" aria-label="News feed"><span></span></a>
  <div class="footer-bottom">
    <div>Home<span class="sep">|</span>Fitness<span class="sep">|</span>Nutrition<span class="sep">|</span>Fit Lounge<span class="sep">|</span>Fit Score<span class="sep">|</span>Fit School<span class="sep">|</span>Contact Us<span class="sep">|</span>Sign Up</div>
    <div>Privacy Policy<span class="sep">|</span>Terms and Conditions</div>
    <div>Copyright © 2012 travlinfit.com <span class="sep">|</span> All rights reserved.</div>
  </div>
</footer>

</body>
</html>
```